Fresh-looking quality Label Design needed for Matcha Supplement

We need a Label Design for our new product Lumo Tab, a Matcha supplement, which uses just the best quality organic matcha from Japan.
We stand for the highest quality of our natural products.
Customers are from the DACH region and our products are slightly more expensive than from competitors.
The design should communicate a healthy lifestyle, high quality and the natural origin of the product, while also having a fresh and young touch. Designs for Inspiration are added in the files. Please take a look at them.
We think green colors work great, but the designer is free to choose colors he sees as a good fit. Brava Nuvio Sana Logo can also be used in black&white if that leads to a better-looking result.
The product text is fully in German and provided in the text file in the uploaded documents. There is only the need to copy and paste.
The center part of the product should be more visual (similar to the example uploads). We do not have a logo for the product name Lumo Tab, but it should just be "Lumo Tab" in a fitting font and in a green color. Font and logo should fit the overall design.
The side parts should include the rest of the text. The arrangement can be chosen as the designer sees fit, but the main layout should be appropriate for a product label.
All the text in the text document must be used. Text in Brackets "()" is just for better structure and should not be included on the finished design.
The product is of organic quality and completely vegan. The necessary bio seals and the vegan logo are in the uploaded documents and should all be used.
Product label dimensions: 140x55mm
Design should not look like a medical product, nor like an overly flashy gym supplement.
Industry/Entity Type
Supplement
Font styles to use
Colors
Designer to choose colors to be used in the design.
Look and feel
Each slider illustrates characteristics of the customer's brand and the style your logo design should communicate.

```html
<!DOCTYPE html>
<html lang="de">
<head>
<meta charset="utf-8">
<title>Lumo Tab – Etikett</title>
<link href="https://fonts.googleapis.com/css2?family=Comfortaa:wght@400&family=Open+Sans:wght@400;600;700&display=swap" rel="stylesheet">
<style>
  :root {
    --green-dark: #6f9a32;
    --green: #86b23a;
    --green-light: #a9c94a;
    --green-text: #7a9e35;
    --ink: #1b1b1b;
    --white: #ffffff;
    --paper: #f4f4f4;
    --grey: #d9d9d9;
    --logo-bg: #000000;
    --logo-ink: #4cc3c9;
  }
  html, body { margin: 0; padding: 0; width: 1200px; height: 1182px; overflow: hidden; background: var(--white); }
  body { position: relative; font-family: "Open Sans", sans-serif; color: var(--ink); }
  .label {
    position: absolute; left: 30px; top: 402px;
    width: 1300px; height: 430px;
    transform: scale(0.877); transform-origin: 0 0;
    overflow: hidden;
    box-shadow: 0 6px 14px rgba(0,0,0,0.18);
  }
  .label-bg { position: absolute; inset: 0; }
  .abs { position: absolute; }

  /* left panel */
  .usage-title { left: 30px; top: 26px; width: 340px; text-align: center; color: var(--green-text); font-size: 20px; letter-spacing: 0.5px; }
  .usage-box { left: 30px; top: 54px; width: 340px; height: 46px; border-left: 5px solid var(--green-dark); border-right: 5px solid var(--green-dark); box-sizing: border-box; padding: 0 8px; }
  .usage-box p { margin: 0; height: 100%; background: var(--green-dark); color: var(--white); font-size: 17.5px; line-height: 21px; text-align: center; padding-top: 2px; box-sizing: border-box; margin: 0 3px; }
  .notice { left: 30px; top: 110px; width: 342px; margin: 0; font-size: 16px; line-height: 20.4px; text-align: justify; }
  .quantity { left: 30px; top: 376px; font-size: 18px; font-weight: 700; }
  .quantity .big { font-size: 38px; vertical-align: -4px; }
  .seal { border-radius: 4px; }

  /* centre */
  .brand { left: 525px; top: 110px; font-family: "Comfortaa", sans-serif; font-size: 62px; line-height: 1; letter-spacing: 1px; }
  .brand .first { color: var(--green-text); }
  .brand .second { color: var(--white); }
  .brand sup { font-size: 22px; vertical-align: 36px; color: var(--white); }
  .maker { left: 543px; top: 252px; width: 185px; height: 113px; background: var(--logo-bg); display: flex; align-items: center; justify-content: center; gap: 10px; }
  .maker .dot { width: 14px; height: 14px; border-radius: 50%; background: var(--logo-ink); flex: none; }
  .maker .name { color: var(--logo-ink); font-size: 17px; font-weight: 600; line-height: 22px; }
  .tagline { left: 510px; top: 404px; font-size: 18px; }

  /* right panel */
  .claim { left: 912px; top: 22px; width: 358px; height: 64px; background: var(--white); color: var(--green-text); font-size: 21px; line-height: 24px; text-align: center; padding-top: 7px; box-sizing: border-box; }
  .facts-head { left: 918px; top: 94px; color: var(--white); font-size: 18px; white-space: pre; }
  .facts { left: 912px; top: 124px; width: 355px; border: 2px solid var(--white); border-collapse: collapse; color: var(--white); font-size: 19px; }
  .facts td { padding: 1px 6px; border-bottom: 1px solid var(--white); height: 25px; }
  .facts td.amount { text-align: right; }
  .facts td.nrv { text-align: center; font-size: 14px; vertical-align: top; }
  .facts tr:last-child td { border-bottom: none; }
  .notes { left: 912px; top: 250px; width: 375px; margin: 0; color: var(--white); font-size: 14.5px; line-height: 19px; }
  .notes b { font-weight: 700; }
  .contact { left: 912px; top: 372px; color: var(--white); font-size: 18px; line-height: 21px; }
  .cert { left: 1210px; top: 355px; width: 60px; height: 60px; border-radius: 50%; background: var(--white); border: 3px solid var(--green-light); box-sizing: border-box; }
</style>
</head>
<body>
  <div class="label">
    <svg class="label-bg" width="1300" height="430" viewBox="0 0 1300 430">
      <defs>
        <linearGradient id="paperGrad" x1="0" x2="1" y1="0" y2="0">
          <stop offset="0" stop-color="#d6d6d6"/>
          <stop offset="0.3" stop-color="#f6f6f6"/>
          <stop offset="1" stop-color="#ffffff"/>
        </linearGradient>
        <linearGradient id="greenGrad" x1="0" x2="1" y1="0" y2="0">
          <stop offset="0" stop-color="#a9c94a"/>
          <stop offset="0.45" stop-color="#8ab53e"/>
          <stop offset="1" stop-color="#6f9a32"/>
        </linearGradient>
      </defs>
      <rect width="1300" height="430" fill="url(#paperGrad)"/>
      <path d="M680 0 C760 70 740 260 520 385 C480 405 460 420 450 430 L1300 430 L1300 0 Z" fill="#d8e6a6"/>
      <path d="M705 0 C780 80 760 270 545 390 C505 410 485 422 475 430 L1300 430 L1300 0 Z" fill="url(#greenGrad)"/>
      <rect x="860" y="0" width="440" height="430" fill="#7ba537" opacity="0.35"/>
      <!-- illustration areas -->
      <rect x="500" y="28" width="100" height="50" rx="25" fill="#cfcfcf" opacity="0.5" role="img" aria-label="Gezeichnete Teeblätter"/>
      <rect x="630" y="60" width="55" height="38" rx="19" fill="#cfcfcf" opacity="0.5" role="img" aria-label="Gezeichnetes Teeblatt"/>
      <rect x="405" y="215" width="120" height="80" rx="30" fill="#cfcfcf" opacity="0.45" role="img" aria-label="Gezeichnete Kirschblütenzweige"/>
      <rect x="420" y="285" width="45" height="80" rx="22" fill="#cfcfcf" opacity="0.45" role="img" aria-label="Gezeichnetes Teeblatt"/>
      <rect x="735" y="25" width="75" height="75" rx="35" fill="#ffffff" opacity="0.25" role="img" aria-label="Gezeichnete Kirschblüten"/>
      <rect x="750" y="205" width="40" height="100" rx="20" fill="#ffffff" opacity="0.25" role="img" aria-label="Gezeichnetes Teeblatt"/>
      <rect x="715" y="290" width="115" height="110" rx="40" fill="#ffffff" opacity="0.22" role="img" aria-label="Gezeichnete Kirschblüten"/>
    </svg>

    <div class="abs usage-title">VERZEHREMPFEHLUNG</div>
    <div class="abs usage-box"><p>2 Kapseln täglich mit ausreichend Flüssigkeit einnehmen.</p></div>
    <p class="abs notice">Nahrungsergänzungsmittel sollten nicht als Ersatz für eine abwechslungsreiche und ausgewogene Ernährung und eine gesunde Lebensweise verwendet werden. Die angegebene empfohlene tägliche Verzehrmenge darf nicht überschritten werden. Das Produkt bitte außerhalb der Reichweite von Kleinkindern aufbewahren. Für Kinder und Schwangere nicht empfohlen. Kühl, trocken und lichtgeschützt aufbewahren. Mindestens haltbar bis Ende: siehe Bodenaufdruck.</p>
    <div class="abs quantity">60 Kapseln • <span class="big">℮24g</span></div>
    <div class="abs seal" style="left:263px;top:366px;width:45px;height:52px;background:#ffffff;border:2px solid #c9c9c9;box-sizing:border-box;"></div>
    <div class="abs seal" style="left:316px;top:370px;width:56px;height:38px;background:#7fb536;"></div>

    <div class="abs" style="left:402px;top:33px;width:72px;height:66px;border-radius:50%;background:#ffffff;border:4px solid #7fb536;box-sizing:border-box;"></div>

    <div class="abs brand"><span class="first">Lumo</span> <span class="second">Tab</span><sup>®</sup></div>
    <div class="abs maker"><span class="dot"></span><span class="name">Brava<br>Nuvio<br>Sana</span></div>
    <div class="abs tagline">mit japanischem Bio Matcha</div>

    <div class="abs claim">Nahrungsergänzungsmittel mit<br>100% japanischem Bio Matcha</div>
    <div class="abs facts-head">Nährwerte      je Tagesdosis*   % NRV**</div>
    <table class="abs facts">
      <tr><td>Bio Matcha</td><td class="amount">600mg</td><td class="nrv">****</td></tr>
      <tr><td>davon Polyphenole</td><td class="amount">175mg</td><td class="nrv">****</td></tr>
      <tr><td>davon Katechine</td><td class="amount">103mg</td><td class="nrv">****</td></tr>
      <tr><td>davon EGCG</td><td class="amount">48mg</td><td class="nrv">****</td></tr>
    </table>
    <p class="abs notes">*Entspricht 2 Kapseln. **Prozentsatz der Nährstoffbezugswerte gem. VO (EU) Nr. 1169/2011. ***Keine Nährstoffbezugswerte bekannt.<br><b>Zutaten:</b> Matcha aus kontrolliert biologischem Anbau (kbA, BIO) in Kyushu (Japan), vegane Kapsel: Hydroxypropylmethylcellulose (HPMC).</p>
    <div class="abs contact">Kontakt: Brava Nuvio Sana<br>Lindenweg 12, 4020 Linz</div>
    <div class="abs cert"></div>
  </div>
</body>
</html>
```